Dental Office Looking for Modern, simple business cards

We just acquired our logo. Now we would like to make business cards. We are a dental office with two doctors. We are husband and wife and have a small boutique dental practice in a small town. We love our patients and they are always asking us to give our business cards to their friends. Please help us make business cards :-)

Target Market(s)

30-60 yr old

Industry/Entity Type

Dental Clinic

Contact Information for Business Card

Birch Hollow Dental P.C.
Family and Cosmetic Dentistry
4827 Dunmore Rd. Schenectady NY 12309
Tel: 518 642 8817 Fax: 518 642 8830

Dr. Tomas K. Elridge DDS
Dr. Marisol Anne Whitby DDS

Font styles to use
Serif
Sans Serif

Requirements
Must have
• Simple clean design, modern, colorful. Should incorporate the logo.
Nice to have
• dental imagery ( teeth, smile, etc ...).

```html
<!DOCTYPE html>
<html lang="en">
<head>
<meta charset="utf-8">
<title>Birch Hollow Dental – Business Cards</title>
<link href="https://fonts.googleapis.com/css2?family=Poppins:wght@400;500;600&display=swap" rel="stylesheet">
<style>
  :root {
    --stage: #10294a;
    --paper: #ffffff;
    --brand-blue: #1f7fc5;
    --brand-deep: #1b68a8;
    --ink-white: #ffffff;
    --rule-grey: #8a8f96;
  }
  * { margin: 0; padding: 0; box-sizing: border-box; }
  html, body { width: 1200px; height: 900px; overflow: hidden; }
  body {
    background: var(--stage);
    font-family: "Poppins", Arial, sans-serif;
    position: relative;
  }
  .card {
    position: absolute;
    width: 600px;
    height: 343px;
    background: var(--paper);
    border-radius: 30px;
    overflow: hidden;
    box-shadow: 0 18px 40px rgba(0, 0, 0, 0.35);
  }
  .card-front { left: 100px; top: 90px; }
  .card-back  { left: 500px; top: 467px; }
  .card-art { position: absolute; inset: 0; width: 100%; height: 100%; }

  .brand {
    position: absolute;
    display: flex;
    align-items: center;
    gap: 10px;
    color: var(--brand-blue);
    font-weight: 500;
    white-space: nowrap;
  }
  .brand-dot {
    border-radius: 50%;
    background: var(--brand-blue);
    flex: none;
  }
  .card-front .brand { left: 150px; top: 104px; font-size: 30px; letter-spacing: 0.5px; }
  .card-front .brand-dot { width: 18px; height: 18px; }
  .card-back .brand { left: 40px; top: 56px; font-size: 19px; letter-spacing: 0.3px; }
  .card-back .brand-dot { width: 12px; height: 12px; }

  .holder {
    position: absolute;
    left: 330px;
    top: 42px;
    color: var(--ink-white);
  }
  .holder-name { font-size: 16px; font-weight: 600; letter-spacing: 0.3px; }
  .holder-role { font-size: 10px; font-weight: 400; letter-spacing: 0.4px; margin-top: 1px; }

  .contact-list {
    position: absolute;
    left: 412px;
    top: 196px;
    list-style: none;
    color: var(--ink-white);
    font-size: 9.5px;
    letter-spacing: 0.4px;
    line-height: 1.45;
  }
  .contact-list li { display: flex; align-items: center; gap: 8px; margin-bottom: 3px; }
  .contact-list svg { width: 10px; height: 10px; flex: none; }
  .contact-list .address { align-items: flex-start; }
  .contact-list .address svg { margin-top: 3px; }
</style>
</head>
<body>

  <section class="card card-front" aria-label="Business card front">
    <svg class="card-art" viewBox="0 0 600 343" aria-hidden="true">
      <path d="M95 343 C165 255 300 250 430 220 C500 204 520 110 600 60 L600 343 Z" fill="var(--brand-blue)"/>
      <path d="M430 220 C500 204 520 110 600 60 L600 40 C535 75 505 170 440 214 Z" fill="var(--brand-deep)"/>
      <path d="M430 220 C480 180 520 100 600 62 L600 78 C535 110 500 190 430 220 Z" fill="var(--brand-deep)" opacity="0.6"/>
    </svg>
    <div class="brand"><span class="brand-dot"></span>Birch Hollow Dental</div>
  </section>

  <section class="card card-back" aria-label="Business card back">
    <svg class="card-art" viewBox="0 0 600 343" aria-hidden="true">
      <path d="M270 0 C290 60 340 90 380 125 C410 160 405 270 440 343 L600 343 L600 0 Z" fill="var(--brand-blue)"/>
      <path d="M270 0 C290 60 340 90 380 125 C395 140 402 160 405 180 C390 140 350 110 320 80 C295 55 280 30 276 0 Z" fill="var(--brand-deep)"/>
    </svg>
    <div class="brand"><span class="brand-dot"></span>Birch Hollow Dental</div>

    <div class="holder">
      <p class="holder-name">Dr. Tomas K. Elridge DDS</p>
      <p class="holder-role">Managing Director</p>
    </div>

    <ul class="contact-list">
      <li>
        <svg viewBox="0 0 10 10"><path d="M2 1 L4 1 L4.6 3.2 L3.4 4 C4 5.4 4.8 6.2 6 6.8 L6.8 5.6 L9 6.2 L9 8.2 C9 8.8 8.5 9 8 9 C4.5 8.8 1.2 5.5 1 2 C1 1.5 1.4 1 2 1 Z" fill="var(--ink-white)"/></svg>
        518 642 8817
      </li>
      <li>
        <svg viewBox="0 0 10 10"><rect x="2.5" y="1" width="5" height="3" fill="var(--ink-white)"/><rect x="1" y="4" width="8" height="4" rx="0.8" fill="var(--ink-white)"/><rect x="3" y="6.5" width="4" height="2.5" fill="var(--brand-blue)" stroke="var(--ink-white)" stroke-width="0.8"/></svg>
        518 642 8830
      </li>
      <li>
        <svg viewBox="0 0 10 10"><rect x="1" y="2" width="8" height="6" fill="none" stroke="var(--ink-white)" stroke-width="1"/><path d="M1 2 L5 5.5 L9 2" fill="none" stroke="var(--ink-white)" stroke-width="1"/></svg>
        tomas@bhdental.com
      </li>
      <li>
        <svg viewBox="0 0 10 10"><circle cx="5" cy="5" r="4" fill="none" stroke="var(--ink-white)" stroke-width="1"/><path d="M1 5 H9 M5 1 C3 3.5 3 6.5 5 9 M5 1 C7 3.5 7 6.5 5 9" fill="none" stroke="var(--ink-white)" stroke-width="0.7"/></svg>
        www.bhdental.com
      </li>
      <li class="address">
        <svg viewBox="0 0 10 10"><path d="M5 9.5 C3 7 1.8 5.3 1.8 3.8 A3.2 3.2 0 0 1 8.2 3.8 C8.2 5.3 7 7 5 9.5 Z" fill="var(--ink-white)"/><circle cx="5" cy="3.8" r="1.2" fill="var(--brand-blue)"/></svg>
        <span>Family and Cosmetic Dentistry<br>4827 Dunmore Rd.<br>Schenectady NY 12309</span>
      </li>
    </ul>
  </section>

</body>
</html>
```